Billboard design for retail kitchen cabinet business

We have a large 7,000 square-foot showroom of beautiful kitchen cabinet displays of all different designs and price ranges. In business for over 50 years with expert designers.
Full size Norvale Media 14' X 48' billboard
Target Market(s)
Retail public on high traffic Los Angeles streets

```html
<!DOCTYPE html>
<html lang="en">
<head>
<meta charset="utf-8">
<title>The Cabinet House — Billboard</title>
<link rel="stylesheet" href="https://fonts.googleapis.com/css2?family=Oswald:wght@400&family=Montserrat:wght@800&display=swap">
<style>
  :root {
    --frame: #3a3a3c;
    --band: #3b3b3d;
    --yellow: #fbb316;
    --orange-deep: #f47b20;
    --white: #ffffff;
  }
  * { margin: 0; padding: 0; box-sizing: border-box; }
  html, body {
    width: 1200px; height: 418px; overflow: hidden;
    background: var(--frame);
  }
  .billboard {
    position: relative; width: 1200px; height: 418px;
    background: var(--frame);
  }
  .artwork { position: absolute; inset: 0; display: block; }
  .brand-name {
    position: absolute; left: 120px; top: 84px;
    font-family: "Oswald", sans-serif; font-weight: 400;
    color: var(--yellow); line-height: 1;
  }
  .brand-name span { display: block; white-space: nowrap; }
  .brand-name .brand-small { font-size: 36px; margin-bottom: 6px; }
  .brand-name .brand-large { font-size: 72px; line-height: 86px; }
  .contact-line {
    position: absolute; left: 74px; top: 318px;
    font-family: "Montserrat", sans-serif; font-weight: 800;
    font-size: 32px; letter-spacing: 0.2px;
    color: var(--yellow); white-space: nowrap; line-height: 38px;
  }
</style>
</head>
<body>
<main class="billboard">
  <svg class="artwork" viewBox="0 0 1200 418" width="1200" height="418" xmlns="http://www.w3.org/2000/svg">
    <defs>
      <clipPath id="panel-clip"><rect x="47" y="48" width="1106" height="322"/></clipPath>
      <linearGradient id="orange-field" x1="0" y1="0" x2="1" y2="0.3">
        <stop offset="0" stop-color="var(--yellow)"/>
        <stop offset="0.55" stop-color="#fbab17"/>
        <stop offset="1" stop-color="var(--orange-deep)"/>
      </linearGradient>
      <linearGradient id="paper-fade" x1="0" y1="0" x2="1" y2="0">
        <stop offset="0" stop-color="#f1efec"/>
        <stop offset="1" stop-color="#fbfbfa"/>
      </linearGradient>
      <linearGradient id="tone-red" x1="0" y1="0" x2="0" y2="1">
        <stop offset="0" stop-color="#8c1d1f"/><stop offset="0.5" stop-color="#a8742f"/><stop offset="1" stop-color="#3a1412"/>
      </linearGradient>
      <linearGradient id="tone-wood" x1="0" y1="0" x2="1" y2="1">
        <stop offset="0" stop-color="#c48a52"/><stop offset="0.5" stop-color="#8a5128"/><stop offset="1" stop-color="#5a3a22"/>
      </linearGradient>
      <linearGradient id="tone-warm" x1="0" y1="0" x2="1" y2="1">
        <stop offset="0" stop-color="#e2b27a"/><stop offset="1" stop-color="#a45b2c"/>
      </linearGradient>
      <linearGradient id="tone-white" x1="0" y1="0" x2="1" y2="1">
        <stop offset="0" stop-color="#e9ecee"/><stop offset="0.6" stop-color="#c9cdd0"/><stop offset="1" stop-color="#2b2b2e"/>
      </linearGradient>
      <linearGradient id="tone-classic" x1="0" y1="0" x2="0" y2="1">
        <stop offset="0" stop-color="#9a6a45"/><stop offset="0.6" stop-color="#7a4424"/><stop offset="1" stop-color="#b48a62"/>
      </linearGradient>
    </defs>

    <g clip-path="url(#panel-clip)">
      <rect class="showroom-backdrop" x="47" y="48" width="1106" height="322" fill="url(#paper-fade)" role="img" aria-label="Faded photo of a white kitchen showroom"/>
      <polygon class="orange-field" points="417,48 1153,48 1153,370 722,370" fill="url(#orange-field)"/>
      <polygon points="722,370 770,330 800,370" fill="var(--white)"/>
      <polygon points="1035,370 1070,330 1080,370" fill="var(--white)"/>

      <g class="photo-tiles" stroke="var(--white)" stroke-width="5">
        <rect x="540" y="-19" width="178" height="178" rx="22" transform="rotate(45 629 70)" fill="url(#tone-red)" stroke="none" role="img" aria-label="Photo of a red modern kitchen with island and bar stool"/>
        <rect x="716" y="104" width="212" height="212" rx="26" transform="rotate(45 822 210)" fill="url(#tone-wood)" role="img" aria-label="Photo of a wood cabinet kitchen with range hood"/>
        <rect x="888" y="68" width="106" height="106" rx="16" transform="rotate(45 941 121)" fill="url(#tone-warm)" role="img" aria-label="Photo of a spacious warm wood kitchen"/>
        <rect x="881" y="204" width="152" height="152" rx="20" transform="rotate(45 957 280)" fill="url(#tone-white)" role="img" aria-label="Photo of a white and black contemporary kitchen island"/>
        <rect x="1003" y="139" width="142" height="142" rx="20" transform="rotate(45 1074 210)" fill="url(#tone-classic)" stroke="none" role="img" aria-label="Photo of a classic carved wood kitchen"/>
      </g>

      <path class="contact-band" d="M47 306 H668 C690 306 702 340 692 370 H47 Z" fill="var(--band)"/>
    </g>
  </svg>

  <h1 class="brand-name">
    <span class="brand-small">THE</span>
    <span class="brand-large">CABINET</span>
    <span class="brand-large">HOUSE</span>
  </h1>

  <p class="contact-line">(310) 555-0184 | cabinethouse.net</p>
</main>
</body>
</html>
```